Fox & Fern honey company needs a label design.

We need a label design for a new honey company, based in the state of Florida called 'Fox & Fern". We are supplying our online customers with the highest quality of the various kinds of raw honey. Our product is honey in the oval hexagon glass jar with black lid. We would like to see designs that use black background with gold font .
In the upper part of the label is gold flying Honey Bee (profile, silhouette). The name of the brand "Fox & Fern" - Caramel font. Additional fonts are Cinzel, Source Sans Pro. Label measurements 2.6" by 3".
Label content:
Fox & Fern
RAW HONEY
wildflower
PURE & NATURAL
made by Florida Bees
foxandfernhoney.com
NET WT 12oz (340g)

The final design should have eye catching, luxurious look.
Updates

Target Market(s)

Luxury

Industry/Entity Type

Food (bee products)

Other font styles liked:
• caramel

Colors

Designer to choose colors to be used in the design.

Requirements
Must have
• Gold letters on black background, Drawing of a bee, flying in profile

```html
<!DOCTYPE html>
<html lang="en">
<head>
<meta charset="utf-8">
<title>Fox &amp; Fern Raw Honey Label</title>
<link rel="stylesheet" href="https://fonts.googleapis.com/css2?family=Cinzel:wght@700&family=Montserrat:wght@400;500;700&display=swap">
<style>
  :root {
    --backdrop: #fecb05;
    --label-black: #000000;
    --gold: #f6c500;
    --gold-deep: #d9a400;
    --gold-light: #ffe14a;
    --comb-tone: #2a2000;
  }
  * { margin: 0; padding: 0; box-sizing: border-box; }
  html, body { width: 1200px; height: 1189px; overflow: hidden; }
  body { background: var(--backdrop); position: relative; font-family: "Montserrat", sans-serif; }

  .label {
    position: absolute; left: 264px; top: 205px; width: 635px; height: 732px;
    background: var(--label-black); color: var(--gold); overflow: hidden;
    box-shadow: 0 14px 18px -8px rgba(90, 60, 0, 0.55);
  }
  .comb-band {
    position: absolute; left: 0; top: 0; width: 635px; height: 170px;
    background: linear-gradient(180deg, var(--comb-tone) 0%, #140f00 55%, rgba(0,0,0,0) 100%);
  }
  .comb-corner {
    position: absolute; bottom: 0; width: 260px; height: 160px;
  }
  .comb-corner.left {
    left: 0;
    background: radial-gradient(ellipse 100% 100% at 0% 100%, var(--comb-tone) 0%, #140f00 50%, rgba(0,0,0,0) 100%);
  }
  .comb-corner.right {
    right: 0;
    background: radial-gradient(ellipse 100% 100% at 100% 100%, var(--comb-tone) 0%, #140f00 50%, rgba(0,0,0,0) 100%);
  }

  .brand-mark {
    position: absolute; left: 290px; top: 128px; width: 56px; height: 56px;
    border-radius: 50%; background: var(--gold);
  }
  .brand-name {
    position: absolute; left: 0; width: 100%; top: 192px; text-align: center;
    font-family: "Cinzel", serif; font-weight: 700; font-size: 54px; color: var(--gold);
    line-height: 1;
  }
  .ribbon { position: absolute; left: 114px; top: 294px; width: 404px; height: 34px; }
  .ribbon-text {
    position: absolute; left: 114px; top: 294px; width: 404px; height: 34px;
    display: flex; align-items: center; justify-content: center;
    font-family: "Montserrat", sans-serif; font-weight: 500; font-size: 27px;
    letter-spacing: 5px; color: var(--label-black);
  }
  .product-name {
    position: absolute; left: 0; width: 100%; top: 326px; text-align: center;
    font-family: "Montserrat", sans-serif; font-weight: 700; font-size: 116px;
    letter-spacing: -7px; line-height: 1; color: var(--gold);
  }
  .variety {
    position: absolute; left: 0; width: 100%; top: 437px; text-align: center;
    font-family: "Cinzel", serif; font-weight: 700; font-size: 44px;
    letter-spacing: 4px; line-height: 1; color: var(--gold-deep);
  }
  .website {
    position: absolute; left: 0; width: 100%; top: 522px; text-align: center;
    font-size: 17px; font-weight: 500; letter-spacing: 8.3px; color: var(--gold);
  }
  .net-weight {
    position: absolute; left: 0; width: 100%; top: 569px; text-align: center;
    font-size: 20px; font-weight: 500; letter-spacing: -0.5px; color: var(--gold);
  }
  .badge {
    position: absolute; border: 4px solid var(--gold); border-radius: 50%;
    display: flex; flex-direction: column; align-items: center; justify-content: center;
    color: var(--gold); font-weight: 700; line-height: 1.05; text-align: center;
  }
  .badge.natural { left: 228px; top: 618px; width: 84px; height: 84px; }
  .badge.natural .big { font-size: 20px; }
  .badge.natural .small { font-size: 10px; }
  .badge.origin { left: 327px; top: 622px; width: 80px; height: 80px; font-weight: 500; }
  .badge.origin .small { font-size: 10px; }
  .badge.origin .mid { font-size: 14px; }
</style>
</head>
<body>
  <main class="label">
    <div class="comb-band" role="img" aria-label="Gold honeycomb outline pattern across the top of the label"></div>
    <div class="comb-corner left" role="img" aria-label="Gold honeycomb outline pattern in the lower left corner"></div>
    <div class="comb-corner right" role="img" aria-label="Gold honeycomb outline pattern in the lower right corner"></div>

    <span class="brand-mark" aria-hidden="true"></span>
    <h1 class="brand-name">Fox &amp; Fern</h1>

    <svg class="ribbon" viewBox="0 0 404 34" aria-hidden="true">
      <defs>
        <linearGradient id="ribbonGold" x1="0" y1="0" x2="1" y2="0">
          <stop offset="0" stop-color="#e6ae00"/>
          <stop offset="0.2" stop-color="#ffe14a"/>
          <stop offset="0.55" stop-color="#f2bd00"/>
          <stop offset="1" stop-color="#e3a800"/>
        </linearGradient>
      </defs>
      <polygon points="14,0 390,0 404,17 390,34 14,34 0,17" fill="url(#ribbonGold)"/>
    </svg>
    <div class="ribbon-text">PURE RAW</div>

    <p class="product-name">HONEY</p>
    <p class="variety">WILDFLOWER</p>
    <p class="website">WWW.FOXANDFERNHONEY.COM</p>
    <p class="net-weight">NET WT 12oz (340g)</p>

    <div class="badge natural"><span class="big">100%</span><span class="small">NATURAL</span></div>
    <div class="badge origin"><span class="small">MADE BY</span><span class="mid">FLORIDA</span><span class="mid">BEES</span></div>
  </main>
</body>
</html>
```